Brand new letterhead, business card, email signature etc.

We are a financial company in London, UK. Our website is www.quorvane.com. We're wanting a complete remodel of the company colours, letter head, business cards, email signatures, etc. Looking to keep the same font for the company name. I have upload a colour palette that we want to work with. We're looking for company letterhead for outgoing letters/ correspondence, letterhead for internal documentation, email signatures, e-letters. etc. Ultimately we will redesign the entire website also. It is important that our clients get a strong, secure, warm, trustworthy, solid feeling and first impression.
Updates

Designs look the same

Target Market(s)

Institutional investors, (ultra) high net worth individuals

Industry/Entity Type

Finance, Invesments banking.

Font styles to use
Other font styles liked:
• Current font is "Champagne & Limousines"

Requirements
Must have
• Must use the colours provided on the PDF uploaded to the portal. The purple = main colour. The red = accent colour.
Nice to have
• Nice to use same font as now for the company name "Marlowin". Font is "Champagne & Limousines". Nice to have some reference to the old logo flower, but only subtle.
Should not have
• Do not use the colour red from our website. Use the colours provided on the colour palette PDF that I uploaded in the portal.

```html
<!DOCTYPE html>
<html lang="en">
<head>
<meta charset="utf-8">
<title>Marlowin Stationery Set</title>
<link href="https://fonts.googleapis.com/css2?family=Josefin+Sans:wght@300;400&family=Questrial&display=swap" rel="stylesheet">
<style>
:root{
  --stage:#656565;
  --paper:#ffffff;
  --plum:#2d0d1b;
  --accent:#e8412c;
  --ink:#2a1a22;
  --muted:#5a4a52;
  --label:#f2f2f2;
}
*{margin:0;padding:0;box-sizing:border-box}
html,body{width:1200px;height:910px;overflow:hidden;background:var(--stage)}
.canvas{position:relative;width:1200px;height:910px;font-family:"Questrial",sans-serif;color:var(--ink)}
.section-label{position:absolute;font-family:"Josefin Sans",sans-serif;font-weight:300;font-size:17px;color:var(--label);transform:translateX(-50%);white-space:nowrap}
.sheet{position:absolute;background:var(--paper);box-shadow:0 6px 22px rgba(0,0,0,.35);overflow:hidden}
.brand{position:absolute;display:flex;align-items:center;font-family:"Josefin Sans",sans-serif;font-weight:300;color:var(--ink);text-transform:uppercase;white-space:nowrap;line-height:1}
.brand-square{border:1px solid var(--ink);flex:none}
.band{position:absolute;left:0;right:0;background:var(--plum)}

/* Letterhead */
.letterhead{left:67px;top:91px;width:517px;height:731px}
.letterhead .brand{left:180px;top:31px;font-size:18px;letter-spacing:3px}
.letterhead .brand-square{width:39px;height:39px;margin-right:9px}
.footer-rule{position:absolute;left:28px;top:659px;width:462px;height:1px;background:var(--accent)}
.footer-rule-strong{position:absolute;left:205px;top:658px;width:107px;height:3px;background:var(--accent)}
.footer-item{position:absolute;top:674px;display:flex;align-items:flex-start;gap:8px;font-family:"Josefin Sans",sans-serif;font-weight:300;font-size:8.3px;line-height:12px;color:var(--muted);white-space:nowrap}
.footer-item svg{width:18px;height:18px;flex:none;margin-top:1px}
.letterhead .band{bottom:0;height:21px}

/* Cards */
.card{left:671px;width:438px;height:250px}
.card-front{top:91px}
.card-back{top:384px}
.card .band.top{top:0;height:9px}
.card .band.bottom{bottom:0;height:8px}
.name-strip{position:absolute;left:27px;top:0;width:23px;height:68px;background:var(--plum)}
.icon-box{position:absolute;left:27px;width:23px;height:22px;background:var(--plum);display:flex;align-items:center;justify-content:center}
.icon-box svg{width:11px;height:11px}
.person-name{position:absolute;left:59px;top:42px;font-size:16px;letter-spacing:.2px;text-transform:uppercase}
.person-role{position:absolute;left:59px;top:64px;font-size:12px}
.contact-line{position:absolute;left:58px;font-size:13px;line-height:17px;white-space:nowrap}
.card-front .brand{left:252px;top:44px;font-size:18px;letter-spacing:3px}
.card-front .brand-square{width:40px;height:40px;margin-right:9px}
.card-back .brand{left:94px;top:94px;font-size:28px;letter-spacing:4px}
.card-back .brand-square{width:61px;height:61px;margin-right:14px}

/* Email signature */
.signature{left:671px;top:704px;width:438px;height:117px;box-shadow:none}
.sig-panel{position:absolute;left:0;top:0;width:81px;height:117px;background:var(--plum);display:flex;flex-direction:column;align-items:center;justify-content:center;gap:6px}
.sig-panel .brand-square{width:40px;height:40px;border-color:var(--paper)}
.sig-panel .sig-brand{font-family:"Josefin Sans",sans-serif;font-weight:300;font-size:8px;letter-spacing:2px;color:var(--paper);text-transform:uppercase}
.sig-name{position:absolute;left:97px;top:13px;font-size:15px;text-transform:uppercase;color:var(--ink)}
.sig-role{position:absolute;left:97px;top:28px;font-family:"Josefin Sans",sans-serif;font-weight:300;font-size:13px;color:var(--ink)}
.sig-rule{position:absolute;left:97px;top:48px;width:142px;height:1px;background:var(--accent)}
.sig-line{position:absolute;left:97px;display:flex;align-items:center;gap:4px;font-size:9.6px;white-space:nowrap;color:var(--ink)}
.sig-line .item{display:inline-flex;align-items:center;gap:3px;margin-right:6px}
.sig-line svg{width:7px;height:7px;flex:none}
</style>
</head>
<body>
<div class="canvas">

  <div class="section-label" style="left:320px;top:49px">Leterhead</div>
  <div class="section-label" style="left:882px;top:49px">Card Front</div>
  <div class="section-label" style="left:882px;top:354px">Card Back</div>
  <div class="section-label" style="left:898px;top:667px">Email Signature</div>

  <!-- Letterhead -->
  <section class="sheet letterhead">
    <div class="brand"><span class="brand-square"></span>Marlowin</div>

    <div class="footer-rule"></div>
    <div class="footer-rule-strong"></div>

    <div class="footer-item" style="left:27px">
      <svg viewBox="0 0 20 20" fill="none" stroke="#2a1a22" stroke-width="1.2"><circle cx="9" cy="9" r="7.5"/><ellipse cx="9" cy="9" rx="3.2" ry="7.5"/><path d="M1.5 9h15M3 5h12M3 13h12"/><path d="M12 12l6 2-2.5 1 2 2.5-1 .8-2-2.5-1 2.2z" fill="#2a1a22"/></svg>
      <div>info@quorvane.com<br>www.quorvane.com</div>
    </div>
    <div class="footer-item" style="left:139px">
      <svg viewBox="0 0 20 20" fill="none" stroke="#2a1a22" stroke-width="1.4"><path d="M10 15s-5-5.2-5-9a5 5 0 0 1 10 0c0 3.8-5 9-5 9z"/><circle cx="10" cy="6" r="1.8"/><path d="M6 15H2l-1.5 4h19L18 15h-4"/></svg>
      <div>Marlowin (IOM) Limited, Tarrant House,<br>Douglas, Isle of Man, IM98 4QT</div>
    </div>
    <div class="footer-item" style="left:323px">
      <svg viewBox="0 0 20 20" fill="none" stroke="#2a1a22" stroke-width="1.4"><path d="M10 15s-5-5.2-5-9a5 5 0 0 1 10 0c0 3.8-5 9-5 9z"/><circle cx="10" cy="6" r="1.8"/><path d="M6 15H2l-1.5 4h19L18 15h-4"/></svg>
      <div>Marlowin Group Limited, 11th Floor,<br>18 Harrow Court, London, EC3N 2LB</div>
    </div>

    <div class="band"></div>
  </section>

  <!-- Card front -->
  <section class="sheet card card-front">
    <div class="band top"></div>
    <div class="name-strip"></div>
    <svg style="position:absolute;left:33px;top:45px;width:11px;height:13px" viewBox="0 0 12 14" fill="none" stroke="#e8412c" stroke-width="1.3"><circle cx="6" cy="4" r="3"/><path d="M1 13c0-3 2.2-5 5-5s5 2 5 5z"/></svg>
    <div class="person-name">Edward Calloway</div>
    <div class="person-role">Managing Director</div>

    <div class="icon-box" style="top:92px"><svg viewBox="0 0 12 12" fill="none" stroke="#e8412c" stroke-width="1.1"><path d="M2.5 1l2 2.4-1 1.3c.7 1.4 1.8 2.5 3.2 3.2l1.3-1 2.4 2-1.2 1.6C5.8 10.3 1.7 6.2 1.1 2.3z"/></svg></div>
    <div class="contact-line" style="top:94px">+00 2200 417781</div>

    <div class="icon-box" style="top:122px"><svg viewBox="0 0 12 12"><rect x="0.5" y="2.5" width="11" height="7" fill="#e8412c"/><path d="M.5 2.5L6 6.8l5.5-4.3" fill="none" stroke="#2d0d1b" stroke-width=".9"/></svg></div>
    <div class="contact-line" style="top:124px">info@quorvane.com</div>

    <div class="icon-box" style="top:150px"><svg viewBox="0 0 12 12" fill="none" stroke="#e8412c" stroke-width="1"><circle cx="6" cy="6" r="5" fill="#e8412c" fill-opacity=".25"/><ellipse cx="6" cy="6" rx="2.2" ry="5"/><path d="M1 6h10M2 3.5h8M2 8.5h8"/></svg></div>
    <div class="contact-line" style="top:152px">www.quorvane.com</div>

    <div class="icon-box" style="top:180px"><svg viewBox="0 0 12 12" fill="none" stroke="#e8412c" stroke-width="1.1"><path d="M6 8.5S3 5.6 3 3.5a3 3 0 0 1 6 0C9 5.6 6 8.5 6 8.5z" fill="#e8412c"/><path d="M3.5 8.5H2L1 11h10l-1-2.5H8.5"/></svg></div>
    <div class="contact-line" style="top:182px">Marlowin Group Limited, 11th Floor,<br>18 Harrow Court, London, EC3N 2LB</div>

    <div class="brand"><span class="brand-square"></span>Marlowin</div>
    <div class="band bottom"></div>
  </section>

  <!-- Card back -->
  <section class="sheet card card-back">
    <div class="band top"></div>
    <div class="brand"><span class="brand-square"></span>Marlowin</div>
    <div class="band bottom"></div>
  </section>

  <!-- Email signature -->
  <section class="sheet signature">
    <div class="sig-panel"><span class="brand-square"></span><span class="sig-brand">Marlowin</span></div>
    <div class="sig-name">Edward Calloway</div>
    <div class="sig-role">Managing Director</div>
    <div class="sig-rule"></div>

    <div class="sig-line" style="top:59px">
      <span class="item"><svg viewBox="0 0 12 12" fill="none" stroke="#e8412c" stroke-width="1.4"><path d="M2.5 1l2 2.4-1 1.3c.7 1.4 1.8 2.5 3.2 3.2l1.3-1 2.4 2-1.2 1.6C5.8 10.3 1.7 6.2 1.1 2.3z"/></svg>+00 2200 417781</span>
      <span class="item"><svg viewBox="0 0 12 12"><rect x="0.5" y="2.5" width="11" height="7" fill="#e8412c"/></svg>info@quorvane.com</span>
      <span class="item"><svg viewBox="0 0 12 12"><circle cx="6" cy="6" r="5" fill="#e8412c"/></svg>www.quorvane.com</span>
    </div>
    <div class="sig-line" style="top:78px">
      <svg viewBox="0 0 12 12" fill="none" stroke="#e8412c" stroke-width="1.4"><circle cx="6" cy="4" r="2.5"/><path d="M1.5 11c0-2.5 2-4 4.5-4s4.5 1.5 4.5 4z"/></svg>Marlowin Group Limited, 11th Floor, 18 Harrow Court, London, EC3N 2LB
    </div>
    <div class="sig-line" style="top:96px">
      <svg viewBox="0 0 12 12" fill="none" stroke="#e8412c" stroke-width="1.4"><circle cx="6" cy="4" r="2.5"/><path d="M1.5 11c0-2.5 2-4 4.5-4s4.5 1.5 4.5 4z"/></svg>Marlowin (IOM) Limited, Tarrant House, Douglas, Isle of Man, IM98 4QT
    </div>
  </section>

</div>
</body>
</html>
```